Business Card Design

Printing and photocopying solutions, computer sales, photocopier sales and service, stationery needs

We aim to be the best for reliability, knowledge, skilled technical ability and highly ethical in business dealings. We would like to present as professional and the key person for dealing with for all customers. We are based in the Solomon Islands and therefore part of a developing country where many services and infrastructures are not in place. We would like to be seen as leading the field with technology and advanced office support. We strongly support the community and education systems with our current services and are seeking to expand the reach to encompass other service offerings

Target Market(s)

Business, Schools, Government offices, Churches, Non-government organisations

Industry/Entity Type

Business

Contact Information for Business Card

Harbor Copy
harborcopy@mailvista.net
+677 7418903 +677 8257164
PO Box 8
Auki, Malaita Province
Solomon Islands

Requirements
Must have
• professional appearance. Some Blue colouring
Must have easy to read phone number so required the phone number to be large font

Must have Shop address as well
Shop 7, Tidewell Building
Auki, Malaita, Solomon Islands
Nice to have
• Keep simple and professional with appearance of the business card styles, use the back of the card for Logo and a list of the basic services that is offered from Harbor Copy

```html
<!DOCTYPE html>
<html lang="en">
<head>
<meta charset="utf-8">
<title>Harbor Copy — Business Card</title>
<link href="https://fonts.googleapis.com/css2?family=Jost:wght@600&family=Arimo:wght@700&family=Noto+Sans:wght@400&display=swap" rel="stylesheet">
<style>
  :root{
    --page:#e6e3de;
    --indigo-deep:#2a1a5e;
    --indigo-mid:#213a8f;
    --night:#121214;
    --charcoal:#3a3a3d;
    --violet:#9b4fb0;
    --white:#ffffff;
    --ink:#111111;
    --icon:#2d1f5e;
  }
  *{margin:0;padding:0;box-sizing:border-box}
  html,body{width:1200px;height:1200px;overflow:hidden;background:var(--page)}
  .sheet{position:relative;width:1200px;height:1200px}
  .card{position:absolute;left:138px;width:918px;height:537px;overflow:hidden;
        box-shadow:0 6px 18px rgba(0,0,0,.35)}
  .card--front{top:40px}
  .card--back{top:622px;height:534px}
  .card__bg{position:absolute;inset:0;width:100%;height:100%}
  .brand-name{position:absolute;font-family:"Jost",sans-serif;font-weight:600;
        color:var(--white);letter-spacing:3px;white-space:nowrap;line-height:1;text-align:center}
  .card--front .brand-name{left:0;right:0;top:72px;font-size:96px}
  .card--back .brand-name{left:54px;width:670px;top:286px;font-size:78px}
  .contact{position:absolute;left:0;right:46px;top:202px;text-align:center;
        font-family:"Noto Sans",sans-serif;font-size:23px;line-height:36px;color:var(--white)}
  .phone{position:absolute;top:418px;height:78px;display:flex;align-items:center;
        font-family:"Arimo",sans-serif;font-weight:700;font-size:34px;color:var(--ink)}
  .phone--primary{left:90px}
  .phone--secondary{left:510px}
  .phone__icon{width:50px;height:44px;margin-right:30px}
  .services{position:absolute;left:54px;width:670px;top:374px;text-align:center;
        font-family:"Noto Sans",sans-serif;font-size:24px;line-height:39px;color:var(--white);
        letter-spacing:.5px}
</style>
</head>
<body>
<div class="sheet">

  <section class="card card--front">
    <svg class="card__bg" viewBox="0 0 918 537" preserveAspectRatio="none" aria-hidden="true">
      <defs>
        <radialGradient id="frontGlow" cx="45%" cy="55%" r="70%">
          <stop offset="0" stop-color="var(--indigo-mid)"/>
          <stop offset="1" stop-color="var(--indigo-deep)"/>
        </radialGradient>
        <linearGradient id="frontDark" x1="0" y1="0" x2="0" y2="1">
          <stop offset="0" stop-color="#2a2a2d"/>
          <stop offset="1" stop-color="var(--night)"/>
        </linearGradient>
      </defs>
      <rect width="918" height="537" fill="url(#frontGlow)"/>
      <path d="M306 0 Q700 90 786 537 L918 537 L918 0 Z" fill="url(#frontDark)"/>
      <path d="M700 0 Q860 40 918 165 L918 0 Z" fill="var(--charcoal)"/>
      <path d="M306 0 Q700 90 786 537" fill="none" stroke="var(--violet)" stroke-width="9"/>
      <path d="M78 418 H460 Q474 418 466 430 L436 484 Q430 496 416 496 H78 Q66 496 66 484 V430 Q66 418 78 418 Z"
            fill="var(--white)" stroke="var(--indigo-deep)" stroke-width="3"/>
      <path d="M512 418 H846 Q858 418 858 430 V484 Q858 496 846 496 H470 Q456 496 463 484 L492 430 Q499 418 512 418 Z"
            fill="var(--white)" stroke="var(--indigo-deep)" stroke-width="3"/>
    </svg>

    <h1 class="brand-name">HARBOR COPY</h1>

    <div class="contact">
      <p>Email : harborcopy@mailvista.net</p>
      <p>Addres : PO Box 8 Auki, Malaita Province Solomon Islands</p>
      <p>Shop Addres : Shop 7, Tidewell Building Auki, Malaita,</p>
      <p>Solomon Islands</p>
    </div>

    <div class="phone phone--primary">
      <svg class="phone__icon" viewBox="0 0 50 44" aria-hidden="true">
        <path d="M3 14 Q25 0 47 14 L44 20 L35 17 L35 12 Q25 9 15 12 L15 17 L6 20 Z" fill="var(--icon)"/>
        <path d="M14 20 H36 L44 40 H6 Z" fill="var(--icon)"/>
        <circle cx="25" cy="30" r="6" fill="var(--white)"/>
        <circle cx="25" cy="30" r="2.5" fill="var(--icon)"/>
      </svg>
      <span>+677 7418903</span>
    </div>

    <div class="phone phone--secondary">
      <svg class="phone__icon" viewBox="0 0 50 44" aria-hidden="true">
        <path d="M3 14 Q25 0 47 14 L44 20 L35 17 L35 12 Q25 9 15 12 L15 17 L6 20 Z" fill="var(--icon)"/>
        <path d="M14 20 H36 L44 40 H6 Z" fill="var(--icon)"/>
        <circle cx="25" cy="30" r="6" fill="var(--white)"/>
        <circle cx="25" cy="30" r="2.5" fill="var(--icon)"/>
      </svg>
      <span>+677 8257164</span>
    </div>
  </section>

  <section class="card card--back">
    <svg class="card__bg" viewBox="0 0 918 534" preserveAspectRatio="none" aria-hidden="true">
      <defs>
        <radialGradient id="backGlow" cx="42%" cy="50%" r="70%">
          <stop offset="0" stop-color="var(--indigo-mid)"/>
          <stop offset="1" stop-color="var(--indigo-deep)"/>
        </radialGradient>
        <linearGradient id="backDark" x1="0" y1="0" x2="0" y2="1">
          <stop offset="0" stop-color="#2a2a2d"/>
          <stop offset="1" stop-color="var(--night)"/>
        </linearGradient>
      </defs>
      <rect width="918" height="534" fill="url(#backGlow)"/>
      <path d="M384 0 Q780 100 864 534 L918 534 L918 0 Z" fill="url(#backDark)"/>
      <path d="M726 0 Q870 40 918 158 L918 0 Z" fill="var(--charcoal)"/>
      <path d="M384 0 Q780 100 864 534" fill="none" stroke="var(--violet)" stroke-width="9"/>
    </svg>

    <h2 class="brand-name">HARBOR COPY</h2>

    <div class="services">
      <p>Photocopying | Printing | Secretarial | Typing</p>
      <p>Stationery Supplies and Office Automation</p>
    </div>
  </section>

</div>
</body>
</html>
```